Golden Years Wellness Roadmap: This is my second book. The first was Eldercare Compass

I need a book cover design for: GOLDEN YEARS WELLNESS ROADMAP: A NO-EXPENSE METHOD FOR FINISHING YOUR LATER-LIFE MOSAIC WITH POOLED KVB CARE SCHEMES by Derek Holloway Neil Osgrove & Martin Quarles. This book is designed for business owners, CEO's, CFO's and Human Resources. The cover needs to be professional and focused on business. The purpose of this book is to educate business owners and their management about a zero cost retiree health plan. This is a first of it's kind solution that every business needs to learn about.

Target Market(s)

Business owners, CEO's, CFO's and Human Resources

Requirements
Nice to have
• I want the design to be clean and professional since it is focused on business executives

```html
<!DOCTYPE html>
<html lang="en">
<head>
<meta charset="utf-8">
<title>Golden Years Wellness Roadmap — Book Cover</title>
<link rel="stylesheet" href="https://fonts.googleapis.com/css2?family=Saira+Extra+Condensed:wght@500;600&family=Montserrat:wght@400;600;700&display=swap">
<style>
  :root {
    --ink-navy: #0f1f33;
    --ink-dark: #1d1d24;
    --title-blue: #1893c2;
    --band-navy: #03134d;
    --paper: #ffffff;
    --sky-deep: #0d3f7c;
    --sky-mid: #1f78c4;
    --sky-light: #5fc6ea;
  }
  * { margin: 0; padding: 0; box-sizing: border-box; }
  html, body { width: 800px; height: 1200px; overflow: hidden; background: var(--paper); }
  .cover { position: relative; width: 800px; height: 1200px; background: var(--paper); }
  .hero-art {
    position: absolute; left: 0; top: 0; width: 800px; height: 555px;
    background:
      radial-gradient(ellipse at 55% 45%, rgba(95,198,234,0.55), transparent 60%),
      linear-gradient(180deg, var(--sky-deep) 0%, var(--sky-mid) 55%, #2d6fb0 80%, #1a3f6e 100%);
  }
  .title-block { position: absolute; left: 0; top: 600px; width: 800px; }
  .title-block svg { display: block; }
  .title-top { font-family: 'Saira Extra Condensed', sans-serif; font-weight: 500; fill: var(--ink-navy); }
  .title-main { font-family: 'Saira Extra Condensed', sans-serif; font-weight: 600; fill: var(--title-blue); }
  .subtitle {
    position: absolute; left: 100px; top: 924px; width: 600px;
    font-family: 'Montserrat', sans-serif; font-weight: 400; font-size: 23px;
    line-height: 32px; text-align: center; color: var(--ink-dark); text-transform: uppercase;
  }
  .subtitle strong { font-weight: 700; }
  .author-band {
    position: absolute; left: 0; top: 1059px; width: 800px; height: 141px;
    background: var(--band-navy); color: var(--paper);
    display: flex; flex-direction: column; justify-content: center; align-items: center;
    font-family: 'Montserrat', sans-serif; font-weight: 600; font-size: 26px;
    letter-spacing: 6px; line-height: 34px; text-transform: uppercase;
  }
</style>
</head>
<body>
<main class="cover">
  <div class="hero-art" role="img" aria-label="Businessman standing atop a staircase before a glowing city skyline with rising arrows and a medical caduceus in blue tones"></div>

  <h1 class="title-block">
    <svg width="800" height="300" viewBox="0 0 800 300" aria-label="Golden Years Wellness Roadmap">
      <text class="title-top" x="93" y="94" font-size="100" textLength="614" lengthAdjust="spacingAndGlyphs">GOLDEN YEARS WELLNESS</text>
      <text class="title-main" x="65" y="290" font-size="240" textLength="683" lengthAdjust="spacingAndGlyphs">ROADMAP</text>
    </svg>
  </h1>

  <p class="subtitle"><strong>A no-expense method</strong> for finishing your later-life mosaic with pooled KVB care schemes</p>

  <footer class="author-band">
    <span>Derek Holloway, Neil Osgrove</span>
    <span>Martin Quarles</span>
  </footer>
</main>
</body>
</html>
```